Chamber of Commerce Web Design Project

We are working with Marigold Chamber of Commerce. They are a new chamber of commerce forming in SoCal.
Some sites to use for inspiration:
https://brevenlochamber.org
https://varnidel.org
https://www.quoratlinchamber.com
https://www.wtchamber.com
https://morvendipcc.org
Thank you for taking the time to consider designing a website for us. We are web developers based in Stockton, CA, USA. Most of our projects go through the same process. Understanding this process may help you win a project with us. We custom-code all of our websites in-house. We don’t have any requirements as to what tools you use for your design, but we prefer Figma files. For any design that we label as four-stars, we send it to the client for review. The client picks the final design they want us to use. Once we complete this process, we will continue to show additional clients all the four-star sites and purchase them later. Your designs will have multiple chances to sell. For better chances of success, we ask that you follow these guidelines.
IMAGES:
If you use any images or icons in the design, we ask that you have a link to the asset so we can purchase the image/icon. Most of the designs we submit do not have the customer’s images on them unless they have some great images. Be creative; show us the feeling you are trying to portray with your image choices. Use any royalty-free site you choose. We subscribe to Adobe and mainly use their images, but we can purchase images outside of Adobe.
PLEASE NOTE: we will not submit designs to clients with watermarks on the images.
FONTS:
We ask that you identify the fonts used in the design. This can be done in a message if you want. We typically use Google Fonts and Adobe Fonts.
CONTENT:
We're always open to different content and ideas. We often submit designs with stock images so the client can see our vision. We typically take pictures after the website launch to use their images with our vision. Lorem Ipsum is fine for paragraphs, but we ask that you write the headers in correct English. We want to be able to show the vision and identify the sections of the website.
INSPIRATION:
We typically add a couple of links in the brief of websites we like to help you get started in your design.
REVISIONS:
We do not often ask for revisions of the designs unless we see something in the design that may not appeal to the client. If there are slight changes that we want to make, we do that in the development process.
FEEDBACK:
We rarely give feedback on designs during the design process. We are working on many website projects and do not have the time to provide feedback. We usually respond if your request is well thought out and asks specific questions, but a note asking “feedback, please” usually goes unanswered.

```html
<!DOCTYPE html>
<html lang="en">
<head>
<meta charset="utf-8">
<title>Marigold Chamber of Commerce</title>
<link href="https://fonts.googleapis.com/css2?family=IBM+Plex+Sans:wght@500;600;700&family=Roboto:wght@400;500;700&display=swap" rel="stylesheet">
<style>
:root{
  --blue:#1766f6;
  --blue-dark:#0f4fd0;
  --gray:#6a6a6a;
  --gray-text:#5a5a5a;
  --light:#eceef1;
  --white:#fff;
  --footer:#5c5c5e;
  --gold:#e0b93a;
}
*{margin:0;padding:0;box-sizing:border-box}
html,body{width:1200px;height:4364px;overflow:hidden}
body{font-family:"Roboto",sans-serif;color:var(--gray-text);background:var(--white);position:relative}
h1,h2,h3{font-family:"IBM Plex Sans",sans-serif}
.btn{position:absolute;display:flex;align-items:center;justify-content:center;font:700 15px "Roboto",sans-serif;text-transform:uppercase;letter-spacing:.3px;color:var(--white)}
.eyebrow{font:500 19px "Roboto",sans-serif;color:var(--blue);text-transform:uppercase;letter-spacing:.4px}
.section-title{font:500 34px "IBM Plex Sans",sans-serif;color:var(--gray-text)}

/* header */
.site-header{position:absolute;left:0;top:0;width:1200px;height:147px;background:var(--white);box-shadow:0 2px 6px rgba(0,0,0,.08);z-index:2}
.topbar{position:absolute;left:0;top:0;width:1200px;height:59px;clip-path:polygon(525px 0,1200px 0,1200px 59px,466px 59px);background:var(--blue)}
.brand{position:absolute;left:110px;top:34px;display:flex;align-items:center;gap:12px}
.brand-mark{width:66px;height:66px;border-radius:50%;background:var(--blue)}
.brand-name{font:700 34px/1 "IBM Plex Sans",sans-serif;color:var(--blue);letter-spacing:.5px}
.brand-name small{display:block;font:700 16px "IBM Plex Sans",sans-serif;margin-top:4px;letter-spacing:.2px}
.social{position:absolute;display:flex;gap:8px}
.social span{width:32px;height:32px;border-radius:50%;border:2px solid var(--white)}
.join-top{left:875px;top:10px;width:212px;height:39px;background:var(--white);color:var(--blue);font-size:16px}
.nav{position:absolute;top:90px;left:0;font:400 16px "Roboto",sans-serif;color:var(--gray-text)}
.nav a{position:absolute;color:inherit;text-decoration:none;white-space:nowrap}
.nav a.active{color:var(--blue);text-decoration:underline;text-underline-offset:4px}

/* hero */
.hero{position:absolute;left:0;top:147px;width:1200px;height:555px;background:linear-gradient(180deg,#3d79d8 0%,#7fa9e6 38%,#5f6f86 60%,#3f4b5e 85%,#2c3646 100%)}
.hero h1{position:absolute;left:110px;top:120px;font:700 52px/57px "IBM Plex Sans",sans-serif;color:var(--white);text-shadow:0 2px 6px rgba(0,0,0,.35)}
.hero p{position:absolute;left:110px;top:306px;width:520px;font:400 17.5px/30px "Roboto",sans-serif;color:var(--white)}
.hero .btn{left:110px;top:387px;width:275px;height:41px;background:var(--white);color:var(--blue);font-size:16px}

/* about */
.about{position:absolute;left:0;top:702px;width:1200px;height:540px;background:var(--white)}
.about-photo{position:absolute;left:180px;top:122px;width:362px;height:362px;border-radius:50%;border:5px solid var(--blue);background:linear-gradient(135deg,#6d5a4a,#b8a58f 50%,#4a4f5c)}
.about .eyebrow{position:absolute;left:600px;top:106px}
.about h2{position:absolute;left:600px;top:142px;width:520px;font-size:34px;line-height:41px}
.about p{position:absolute;left:600px;top:240px;width:490px;font:400 15.5px/25.6px "Roboto",sans-serif}
.about .learn{left:600px;top:391px;width:171px;height:41px;background:var(--blue)}
.about .joinnow{left:788px;top:391px;width:171px;height:41px;background:var(--gray)}

/* membership */
.benefits{position:absolute;left:0;top:1242px;width:1200px;height:1246px;background:var(--light)}
.benefits .eyebrow{position:absolute;left:0;width:1200px;top:66px;text-align:center}
.benefits h2{position:absolute;left:0;width:1200px;top:103px;text-align:center}
.benefits .sub{position:absolute;left:0;width:1200px;top:162px;text-align:center;font-size:15.5px}
.card{position:absolute;width:309px;height:448px;overflow:hidden}
.card .photo{position:absolute;inset:0}
.card .stripe{position:absolute;inset:0;background:var(--white)}
.card .panel{position:absolute;inset:0}
.card.blue .panel{background:var(--blue)}
.card.grey .panel{background:var(--gray)}
.card.one .stripe{clip-path:polygon(0 0,100% 0,100% 244px,0 286px)}
.card.one .panel{clip-path:polygon(0 0,100% 0,100% 232px,0 274px)}
.card.two .stripe{clip-path:polygon(0 0,100% 0,100% 274px,0 316px)}
.card.two .panel{clip-path:polygon(0 0,100% 0,100% 262px,0 304px)}
.card h3{position:absolute;left:24px;top:58px;width:270px;font:500 19.5px/31px "Roboto",sans-serif;color:var(--white);text-transform:uppercase;letter-spacing:.3px}
.card p{position:absolute;left:24px;width:270px;font:400 13.5px/26px "Roboto",sans-serif;color:var(--white)}
.card.one p{top:94px}.card.two p{top:125px}
.card svg.arrow{position:absolute;left:24px}
.card.one svg.arrow{top:185px}.card.two svg.arrow{top:215px}

/* events */
.events{position:absolute;left:0;top:2488px;width:1200px;height:546px;background:var(--blue)}
.events svg.scene{position:absolute;left:0;top:0}
.events .eyebrow{position:absolute;left:110px;top:116px;color:var(--white)}
.events h2{position:absolute;left:110px;top:152px;font:600 33px "IBM Plex Sans",sans-serif;color:var(--white);white-space:nowrap}
.events p{position:absolute;left:110px;top:207px;width:470px;font:400 15px/26px "Roboto",sans-serif;color:var(--white)}
.events .btn{left:110px;top:388px;width:214px;height:39px;background:var(--gray)}

/* testimonials */
.testimonials{position:absolute;left:0;top:3034px;width:1200px;height:814px;background:linear-gradient(180deg,#f2f3f4 0%,#eceeef 45%,#dcdfe2 100%)}
.testimonials .eyebrow{position:absolute;left:0;width:1216px;top:80px;text-align:center}
.testimonials h2{position:absolute;left:0;width:1220px;top:118px;text-align:center}
.quote-card{position:absolute;top:268px;width:443px;height:376px;background:var(--white);border-radius:18px 18px 60px 18px;box-shadow:0 6px 18px rgba(0,0,0,.08)}
.quote-card svg.q{position:absolute;left:38px;top:42px}
.avatar{position:absolute;top:-65px;left:156px;width:130px;height:130px;border-radius:50%;border:3px solid var(--blue);background:var(--white);padding:5px}
.avatar div{width:100%;height:100%;border-radius:50%;background:linear-gradient(160deg,#9aa3ad,#4f5966)}
.quote-card h3{position:absolute;top:107px;left:0;width:100%;text-align:center;font:500 19px "Roboto",sans-serif;color:#333;text-transform:uppercase}
.stars{position:absolute;top:140px;left:0;width:100%;text-align:center;color:var(--gold);font-size:19px;letter-spacing:4px}
.quote-card p{position:absolute;top:180px;left:30px;width:383px;text-align:center;font:400 15.5px/31px "Roboto",sans-serif;color:#666}
.slider-btn{position:absolute;top:672px;width:60px;height:60px;border-radius:50%}
.slider-btn.prev{left:526px;background:var(--white);border:1px solid #cfd3d8}
.slider-btn.next{left:612px;background:var(--blue)}
.slider-btn svg{position:absolute;left:18px;top:18px}

/* footer */
.footer{position:absolute;left:0;top:3848px;width:1200px;height:516px;background:var(--footer);color:var(--white)}
.footer .brand{left:430px;top:84px}
.footer .brand-name{font-size:56px}
.footer .brand-mark{width:70px;height:70px}
.contact{position:absolute;width:300px;text-align:center}
.contact .ic{width:44px;height:44px;border-radius:50%;background:var(--white);margin:0 auto 12px;display:flex;align-items:center;justify-content:center}
.contact h4{font:500 19.5px "Roboto",sans-serif;text-transform:uppercase;letter-spacing:.4px}
.contact p{font:400 14.5px/23px "Roboto",sans-serif;margin-top:4px}
.footer .social{left:515px;top:402px}
.footer .social span{width:30px;height:30px}
.copy{position:absolute;top:472px;left:0;width:1200px;text-align:center;font-size:14.5px}
</style>
</head>
<body>

<header class="site-header">
  <div class="topbar"></div>
  <div class="brand">
    <div class="brand-mark"></div>
    <div class="brand-name">MARIGOLD<small>CHAMBER OF COMMERCE</small></div>
  </div>
  <div class="social" style="left:641px;top:13px" aria-label="Social links">
    <span></span><span></span><span></span><span></span><span></span>
  </div>
  <a class="btn join-top">Join the Chamber</a>
  <nav class="nav">
    <a class="active" style="left:451px">Home</a>
    <a style="left:539px">About Us</a>
    <a style="left:651px">Resources</a>
    <a style="left:775px">Membership</a>
    <a style="left:912px">Events</a>
    <a style="left:1005px">Contact Us</a>
  </nav>
</header>

<section class="hero" role="img" aria-label="Southern California city skyline under a blue sky">
  <h1>Empowering<br>Business Growth &amp;<br>Community Success</h1>
  <p>Connecting entrepreneurs, fostering innovation, and driving economic development in Southern California.</p>
  <a class="btn">Explore Member Benefits</a>
</section>

<section class="about">
  <div class="about-photo" role="img" aria-label="Business people shaking hands across a meeting table"></div>
  <div class="eyebrow">About Us</div>
  <h2>Building a Stronger Business Community</h2>
  <p>Sed ut perspiciatis unde omnis iste natus error sit voluptatem accusantium doloremque laudantium, totam rem aperiam, eaque ipsa quae ab illo inventore veritatis et quasi architecto beatae vitae dicta sunt explicabo. Nemo enim ipsam voluptatem quia voluptas sit aspernatur aut odit aut fugit</p>
  <a class="btn learn">Learn More</a>
  <a class="btn joinnow">Join Now</a>
</section>

<section class="benefits">
  <div class="eyebrow">Membership Benefits</div>
  <h2 class="section-title">Unlock Opportunities &amp; Grow Your Business</h2>
  <div class="sub">Join a dynamic network of professionals dedicated to success.</div>

  <article class="card blue one" style="left:110px;top:229px">
    <div class="photo" role="img" aria-label="Team meeting around a table" style="background:linear-gradient(135deg,#8a6f55,#c9a57f 50%,#3f4756)"></div>
    <div class="stripe"></div><div class="panel"></div>
    <h3>Membership Benefits</h3>
    <p>Lorem ipsum dolor sit amet, consectetur adipiscing elit, sed do eiusmod tempor incididunt ut labore.</p>
    <svg class="arrow" width="40" height="14" viewBox="0 0 40 14"><path d="M0 7H37M31 1l6 6-6 6" stroke="#fff" stroke-width="2" fill="none"/></svg>
  </article>
  <article class="card grey two" style="left:444px;top:229px">
    <div class="photo" role="img" aria-label="Close-up of a business handshake" style="background:linear-gradient(135deg,#1e2633,#5b6676 50%,#2a3140)"></div>
    <div class="stripe"></div><div class="panel"></div>
    <h3>Business Advocacy and Support</h3>
    <p>Lorem ipsum dolor sit amet, consectetur adipiscing elit, sed do eiusmod tempor incididunt ut labore.</p>
    <svg class="arrow" width="40" height="14" viewBox="0 0 40 14"><path d="M0 7H37M31 1l6 6-6 6" stroke="#fff" stroke-width="2" fill="none"/></svg>
  </article>
  <article class="card blue two" style="left:780px;top:229px">
    <div class="photo" role="img" aria-label="Woman presenting marketing charts on a screen" style="background:linear-gradient(135deg,#a47a5a,#dfe6ee 50%,#7f98b8)"></div>
    <div class="stripe"></div><div class="panel"></div>
    <h3>Marketing &amp; Promotion Opportunities</h3>
    <p>Lorem ipsum dolor sit amet, consectetur adipiscing elit, sed do eiusmod tempor incididunt ut labore.</p>
    <svg class="arrow" width="40" height="14" viewBox="0 0 40 14"><path d="M0 7H37M31 1l6 6-6 6" stroke="#fff" stroke-width="2" fill="none"/></svg>
  </article>

  <article class="card grey one" style="left:110px;top:711px">
    <div class="photo" role="img" aria-label="Small business owner with a tablet among shipping boxes" style="background:linear-gradient(135deg,#b89672,#e3d7c8 50%,#8aa0b4)"></div>
    <div class="stripe"></div><div class="panel"></div>
    <h3>Small Business Help</h3>
    <p>Lorem ipsum dolor sit amet, consectetur adipiscing elit, sed do eiusmod tempor incididunt ut labore.</p>
    <svg class="arrow" width="40" height="14" viewBox="0 0 40 14"><path d="M0 7H37M31 1l6 6-6 6" stroke="#fff" stroke-width="2" fill="none"/></svg>
  </article>
  <article class="card blue two" style="left:444px;top:711px">
    <div class="photo" role="img" aria-label="Person attending an online video conference" style="background:linear-gradient(135deg,#2b3648,#6a7f98 50%,#1c2230)"></div>
    <div class="stripe"></div><div class="panel"></div>
    <h3>Access to Business Education &amp; Resources</h3>
    <p>Lorem ipsum dolor sit amet, consectetur adipiscing elit, sed do eiusmod tempor incididunt ut labore.</p>
    <svg class="arrow" width="40" height="14" viewBox="0 0 40 14"><path d="M0 7H37M31 1l6 6-6 6" stroke="#fff" stroke-width="2" fill="none"/></svg>
  </article>
  <article class="card grey two" style="left:780px;top:711px">
    <div class="photo" role="img" aria-label="Two colleagues reviewing a tablet in an office" style="background:linear-gradient(135deg,#8c7a68,#d8c9b3 50%,#6c5a48)"></div>
    <div class="stripe"></div><div class="panel"></div>
    <h3>Discounted Services Partner Organizations</h3>
    <p>Lorem ipsum dolor sit amet, consectetur adipiscing elit, sed do eiusmod tempor incididunt ut labore.</p>
    <svg class="arrow" width="40" height="14" viewBox="0 0 40 14"><path d="M0 7H37M31 1l6 6-6 6" stroke="#fff" stroke-width="2" fill="none"/></svg>
  </article>
</section>

<section class="events">
  <svg class="scene" width="1200" height="546" viewBox="0 0 1200 546">
    <defs>
      <linearGradient id="eventPhoto" x1="0" y1="0" x2="1" y2="1">
        <stop offset="0" stop-color="#c9b58e"/>
        <stop offset=".45" stop-color="#8a7564"/>
        <stop offset="1" stop-color="#3b3a40"/>
      </linearGradient>
    </defs>
    <polygon points="716,0 1200,0 1200,546 716,546 606,273" fill="#fff"/>
    <g role="img" aria-label="Crowd of visitors walking through a trade fair hall">
      <polygon points="734,0 1200,0 1200,546 734,546 624,273" fill="url(#eventPhoto)"/>
    </g>
  </svg>
  <div class="eyebrow">Events &amp; Programs</div>
  <h2>Stay Connected, Stay Informed</h2>
  <p>Lorem ipsum dolor sit amet, consectetur adipiscing elit, sed do eiusmod tempor incididunt ut labore et dolore magna aliqua. Ut enim ad minim veniam, quis nostrud exercitation ullamco laboris nisi ut aliquip ex ea commodo consequat. Duis aute irure dolor in reprehenderit in voluptate velit esse cillum dolore eu fugiat nulla pariatur.</p>
  <a class="btn">View Our Events</a>
</section>

<section class="testimonials" role="group" aria-label="Member testimonials over a faint mountain landscape">
  <div class="eyebrow">What Our Members Say</div>
  <h2 class="section-title">Building Connections, Creating Opportunities</h2>

  <article class="quote-card" style="left:147px">
    <div class="avatar"><div role="img" aria-label="Portrait of member"></div></div>
    <svg class="q" width="72" height="56" viewBox="0 0 72 56"><path d="M0 14Q0 0 16 0H30V56H0ZM42 14Q42 0 58 0H72V56H42Z" fill="#e6e7e9"/></svg>
    <h3>John Doe</h3>
    <div class="stars">★★★★★</div>
    <p>Sed ut perspiciatis unde omnis iste natus error sit voluptatem accusantium doloremque laudantium, totam rem aperiam, eaque ipsa quae ab illo inventore veritatis et quasi architecto</p>
  </article>
  <article class="quote-card" style="left:610px">
    <div class="avatar"><div role="img" aria-label="Portrait of member" style="background:linear-gradient(160deg,#d9c9a4,#b8543e)"></div></div>
    <svg class="q" width="72" height="56" viewBox="0 0 72 56"><path d="M0 14Q0 0 16 0H30V56H0ZM42 14Q42 0 58 0H72V56H42Z" fill="#e6e7e9"/></svg>
    <h3>Rena Calloway</h3>
    <div class="stars">★★★★★</div>
    <p>Sed ut perspiciatis unde omnis iste natus error sit voluptatem accusantium doloremque laudantium, totam rem aperiam, eaque ipsa quae ab illo inventore veritatis et quasi architecto beatae vitae dicta sunt explicabo.</p>
  </article>

  <a class="slider-btn prev" aria-label="Previous"><svg width="24" height="24" viewBox="0 0 24 24"><path d="M21 12H4M10 6l-6 6 6 6" stroke="#1766f6" stroke-width="2.4" fill="none"/></svg></a>
  <a class="slider-btn next" aria-label="Next"><svg width="24" height="24" viewBox="0 0 24 24"><path d="M3 12H20M14 6l6 6-6 6" stroke="#fff" stroke-width="2.4" fill="none"/></svg></a>
</section>

<footer class="footer">
  <div class="brand">
    <div class="brand-mark"></div>
    <div class="brand-name">MARIGOLD</div>
  </div>

  <div class="contact" style="left:187px;top:242px">
    <div class="ic"><svg width="22" height="22" viewBox="0 0 24 24"><path d="M6.6 10.8a15 15 0 0 0 6.6 6.6l2.2-2.2c.3-.3.7-.4 1-.2 1.1.4 2.3.6 3.6.6.6 0 1 .4 1 1V20c0 .6-.4 1-1 1A17 17 0 0 1 3 4c0-.6.4-1 1-1h3.5c.6 0 1 .4 1 1 0 1.3.2 2.5.6 3.6.1.3 0 .7-.2 1z" fill="#5c5c5e"/></svg></div>
    <h4>Phone</h4>
    <p>+1 555 014 2290</p>
  </div>
  <div class="contact" style="left:436px;top:216px">
    <div class="ic"><svg width="22" height="22" viewBox="0 0 24 24"><path d="M12 2a7 7 0 0 0-7 7c0 5 7 13 7 13s7-8 7-13a7 7 0 0 0-7-7zm0 9.5A2.5 2.5 0 1 1 12 6.5a2.5 2.5 0 0 1 0 5z" fill="#5c5c5e"/></svg></div>
    <h4>Location</h4>
    <p>United States,<br>Chamber of Commerce.</p>
  </div>
  <div class="contact" style="left:699px;top:238px">
    <div class="ic"><svg width="22" height="22" viewBox="0 0 24 24"><path d="M3 5h18v14H3zM3 5l9 8 9-8" stroke="#5c5c5e" stroke-width="2" fill="none"/></svg></div>
    <h4>E-mail</h4>
    <p>hello@marigoldchamber.org</p>
  </div>

  <div class="social" aria-label="Social links">
    <span></span><span></span><span></span><span></span><span></span>
  </div>
  <div class="copy">© 2025 Marigold Chamber of Commerce. All Rights Reserved.</div>
</footer>

</body>
</html>
```